Founder / concept developer needs business card // Consultant needs VCARD

I need a business card for me as a founding consultant in Berlin. I advise entrepreneurs, especially in the design of business ideas, business plans or financing applications. More information about this in the annexes. My USP: I design / structure complex ideas and projects convincingly so that my client is successful. I want to communicate professionalism, effectiveness and clarity. Colors like from the range BLACK-GRAY-GREEN. I am 27 years old, I have studied business for 7 years. Attachments: - Business card design (only idea, do not focus on it) - Website screenshot (only idea, do not focus on it)

Target Market(s)

Target group: Founder (20-50 yrs, m / w, needy, in "break-up phase") and CONTRACTOR / "financier" (30-55 yrs, m / w, often public service "routine-oriented"). The foundations are in quite different industries: digital, craft, tourism, retail, services, etc. Almost all German.

Industry/Entity Type

Consultant

Contact Information for Business Card

Lukas Brandvik
M. Sc., International Business Administration
Gründungsberater, Konzeptentwickler
www.falkenhorn-beratung.de
kontakt@falkenhorn-beratung.de
Tel. 0471 239 5518

Colors

Designer to choose colors to be used in the design.

Requirements
Must have
• Professionalism, persuasiveness, clarity
Nice to have
• memorability
Should not have
• Schnörkelei

```html
<!DOCTYPE html>
<html lang="de">
<head>
<meta charset="utf-8">
<title>Lukas Brandvik – Visitenkarte</title>
<link rel="stylesheet" href="https://fonts.googleapis.com/css2?family=Noto+Serif:wght@400&family=Open+Sans:wght@400&display=swap">
<style>
  :root {
    --page-bg: #e9eaeb;
    --card-white: #fbfbfb;
    --brand-green: #3bb54a;
    --ink-dark: #2b2b2b;
    --ink-mid: #555555;
    --rule-gray: #6e6e6e;
    --card-shadow: rgba(0, 0, 0, 0.18);
  }
  * { margin: 0; padding: 0; box-sizing: border-box; }
  html, body {
    width: 1200px;
    height: 873px;
    overflow: hidden;
    background: var(--page-bg);
  }
  .canvas {
    position: relative;
    width: 1200px;
    height: 873px;
  }
  .card {
    position: absolute;
    left: 340px;
    width: 520px;
    height: 336px;
    border-radius: 3px;
    box-shadow: 0 6px 18px var(--card-shadow);
    overflow: hidden;
  }
  .card--front { top: 72px; background: var(--card-white); }
  .card--back  { top: 466px; background: var(--brand-green); }

  /* Front */
  .front-mark {
    position: absolute;
    left: 0;
    top: 0;
    width: 190px;
    height: 100%;
    display: flex;
    align-items: center;
    justify-content: center;
    font-family: "Noto Serif", serif;
    font-size: 24px;
    color: var(--brand-green);
  }
  .front-rule {
    position: absolute;
    left: 200px;
    top: 50px;
    width: 1px;
    height: 236px;
    background: var(--rule-gray);
  }
  .front-info {
    position: absolute;
    left: 226px;
    top: 78px;
    right: 24px;
  }
  .person-name {
    font-family: "Noto Serif", serif;
    font-size: 27px;
    color: var(--brand-green);
    line-height: 1.1;
    margin-bottom: 8px;
  }
  .person-title {
    font-family: "Open Sans", sans-serif;
    font-size: 11.5px;
    color: var(--ink-mid);
    line-height: 1.5;
    margin-bottom: 26px;
  }
  .contact-row {
    display: flex;
    align-items: center;
    gap: 14px;
    font-family: "Noto Serif", serif;
    font-size: 16px;
    color: var(--ink-dark);
    margin-bottom: 12px;
  }
  .contact-icon { width: 18px; height: 18px; flex: none; }

  /* Back */
  .back-url {
    position: absolute;
    left: 36px;
    top: 0;
    height: 100%;
    display: flex;
    align-items: center;
    font-family: "Noto Serif", serif;
    font-size: 21px;
    color: #ffffff;
  }
  .back-mark {
    position: absolute;
    right: 40px;
    top: 0;
    height: 100%;
    display: flex;
    align-items: center;
    font-family: "Noto Serif", serif;
    font-size: 24px;
    color: #ffffff;
  }
</style>
</head>
<body>
<main class="canvas">
  <section class="card card--front" aria-label="Visitenkarte Vorderseite">
    <div class="front-mark">Falkenhorn</div>
    <div class="front-rule"></div>
    <div class="front-info">
      <h1 class="person-name">Lukas Brandvik</h1>
      <p class="person-title">M. Sc., International Business Administration<br>Gründungsberater, Konzeptentwickler</p>
      <p class="contact-row">
        <svg class="contact-icon" viewBox="0 0 18 18" aria-hidden="true">
          <rect x="4.5" y="1.5" width="9" height="15" rx="1.8" fill="none" stroke="#6e6e6e" stroke-width="1.2"/>
          <line x1="7.5" y1="14" x2="10.5" y2="14" stroke="#6e6e6e" stroke-width="1.2"/>
        </svg>
        0471 239 5518
      </p>
      <p class="contact-row">
        <svg class="contact-icon" viewBox="0 0 18 18" aria-hidden="true">
          <circle cx="9" cy="9" r="3" fill="none" stroke="#6e6e6e" stroke-width="1.2"/>
          <path d="M12 9v1.3a2 2 0 0 0 4 0V9a7 7 0 1 0-2.8 5.6" fill="none" stroke="#6e6e6e" stroke-width="1.2"/>
        </svg>
        kontakt@falkenhorn-beratung.de
      </p>
    </div>
  </section>

  <section class="card card--back" aria-label="Visitenkarte Rückseite">
    <p class="back-url">www.falkenhorn-beratung.de</p>
    <div class="back-mark">Falkenhorn</div>
  </section>
</main>
</body>
</html>
```